Amber Ridge Publishing Web Page Design

Design a website for my new start up publishing company - Amber Ridge Publishing, the first work published by ARP with be a new book by T.R. Menshaw called Silent Harbor. The prototype for the book cover is attached.

Target Market(s)

Worldwide, all readers of mystery, fiction, etc.

Industry/Entity Type

Book Publisher

Coding

Coded - Design and coding required

Number of Pages Required

1 page

```html
<!DOCTYPE html>
<html lang="en">
<head>
<meta charset="utf-8">
<title>Amber Ridge Publishing</title>
<link href="https://fonts.googleapis.com/css2?family=Raleway:wght@400;600;700;800&family=Open+Sans:wght@400;600;700&display=swap" rel="stylesheet">
<style>
:root{
  --orange:#f7941d;
  --orange-dark:#e07f0a;
  --ink:#222222;
  --dark:#2b2b2b;
  --darker:#1c1c1c;
  --grey:#777777;
  --light:#f4f4f4;
  --line:#e2e2e2;
  --white:#ffffff;
}
*{box-sizing:border-box;margin:0;padding:0}
html,body{width:1200px;height:5014px;overflow:hidden}
body{font-family:"Open Sans",Arial,sans-serif;color:var(--ink);background:var(--white);font-size:12px;position:relative}
h1,h2,h3,h4{font-family:"Raleway",Arial,sans-serif}
.section{position:absolute;left:0;width:1200px;overflow:hidden}
.abs{position:absolute}
.center{text-align:center;left:0;width:1200px}
.sec-title{font-size:24px;font-weight:700;color:var(--ink)}
.sec-sub{font-size:11px;color:var(--grey)}
.divider{width:20px;height:10px;border:2px solid var(--grey);border-top:none;margin:8px auto 0;border-radius:0 0 4px 4px}
.on-dark .sec-title{color:var(--white)}
.on-dark .sec-sub{color:#cfcfcf}
.on-dark .divider{border-color:#cfcfcf}
.btn{display:inline-block;background:var(--orange);color:var(--white);font-family:"Raleway",sans-serif;font-weight:700;font-size:11px;text-transform:uppercase;text-align:center}

/* header & hero */
.hero{top:0;height:600px;background:linear-gradient(90deg,#2a2520 0%,#4a4036 45%,#3a332d 100%)}
.hero-photo{position:absolute;inset:0;background:linear-gradient(180deg,rgba(60,52,44,.5),rgba(20,18,16,.7))}
.topbar-note{top:8px;left:470px;font-size:9px;color:var(--orange)}
.topbar-mail{top:8px;left:770px;font-size:9px;color:#ddd}
.logo{top:17px;left:244px;width:124px;height:67px;background:var(--orange);color:var(--white);font-family:"Raleway",sans-serif;font-weight:800;font-size:16px;line-height:19px;padding:12px 10px;text-transform:uppercase}
.nav{top:44px;left:470px;display:flex;gap:22px;font-family:"Raleway",sans-serif;font-size:10px;font-weight:700;color:var(--white)}
.nav .active{color:var(--orange)}
.nav-search{top:36px;left:922px;width:30px;height:30px;background:var(--orange)}
.hero-kicker{top:218px;left:244px;font-family:"Raleway",sans-serif;font-size:19px;color:var(--white)}
.hero-title{top:242px;left:244px;font-size:42px;font-weight:800;color:var(--white);letter-spacing:1px}
.hero-text{top:290px;left:244px;width:420px;font-size:10px;line-height:14px;color:#ddd}
.hero-btn{top:322px;height:26px;line-height:26px;width:86px}
.hero-arrow{top:232px;width:22px;height:36px}
.tabs{top:495px;left:244px;display:flex}
.tab{width:92px;height:28px;line-height:28px;text-align:center;background:var(--white);font-size:10px;font-weight:600}
.tab.active{background:var(--orange);color:var(--white)}
.search-band{top:523px;left:0;width:1200px;height:77px;background:rgba(25,25,25,.92)}
.search-field{top:548px;height:28px;width:160px;border:1px solid #555;color:#aaa;font-size:10px;line-height:26px;padding-left:10px}
.search-btn{top:548px;left:818px;width:142px;height:28px;line-height:28px}

/* welcome */
.welcome{top:600px;height:370px;background:var(--white)}
.feature{top:729px;width:170px;text-align:center}
.feature-icon{width:60px;height:60px;border:1px solid var(--line);margin:0 auto;display:flex;align-items:center;justify-content:center;box-shadow:0 2px 6px rgba(0,0,0,.08)}
.feature h3{font-size:14px;font-weight:700;margin-top:16px}
.feature.hl h3{color:var(--orange)}
.feature p{font-size:9px;color:var(--grey);line-height:13px;margin-top:8px}
.feature .more{font-size:9px;font-weight:700;margin-top:28px}
.feature .more small{display:block;font-weight:400;color:#aaa;font-size:8px}

/* categories */
.categories{top:970px;height:467px;background:var(--dark)}
.cat-filter{top:137px;left:244px;display:flex;height:40px}
.cat-filter span{height:40px;line-height:40px;padding:0 14px;background:var(--white);font-size:9px;color:#555;border-right:1px solid var(--line)}
.cat-filter span.active{background:var(--orange);color:var(--white)}
.book-card{top:207px;width:167px;height:210px;background:var(--white);text-align:center}
.book-card.raised{top:187px;height:243px;width:178px;box-shadow:0 8px 20px rgba(0,0,0,.4)}
.book-cover{height:140px;margin:10px;background:linear-gradient(135deg,#9ea5ad,#5d636a)}
.book-card h4{font-size:10px;font-weight:700}
.book-card .by{font-size:8px;color:var(--grey)}
.book-card .price{font-size:17px;font-weight:700;color:var(--orange);margin-top:4px}
.book-card.raised .blurb{font-size:8px;color:var(--grey);padding:0 14px;line-height:11px;margin-top:4px}
.slide-arrow{top:278px;width:24px;height:24px;background:rgba(255,255,255,.15)}

/* feature band */
.feature-band{top:1437px;height:235px;background:linear-gradient(90deg,#3a3631,#57504a 50%,#3a3631)}
.feature-band h2{font-size:26px;font-weight:700;color:var(--white)}
.outline-btn{top:185px;left:555px;width:90px;height:26px;border:1px solid var(--white);color:var(--white);font-size:9px;line-height:24px;text-align:center}

/* popular */
.popular{top:1672px;height:501px;background:var(--white)}
.pop-tabs{top:143px;left:470px;display:flex;gap:8px}
.pop-tabs span{width:84px;height:22px;line-height:22px;text-align:center;font-size:9px;border:1px solid var(--line);color:#555}
.pop-tabs span.active{background:var(--orange);color:var(--white);border-color:var(--orange)}
.pop-panel{top:177px;left:244px;width:726px;height:290px;border:1px solid var(--line);box-shadow:0 2px 10px rgba(0,0,0,.08)}
.pop-featured-cover{top:24px;left:24px;width:125px;height:190px;background:linear-gradient(135deg,#e8e2d8,#b8ae9e)}
.pop-info{top:24px;left:165px;width:170px}
.pop-info h3{font-size:13px;font-weight:700}
.pop-info .by{font-size:9px;color:var(--grey);margin-top:3px}
.stars{color:var(--orange);font-size:11px;margin-top:4px}
.pop-info p{font-size:9px;color:var(--grey);line-height:13px;margin-top:6px}
.pop-info .price{font-size:17px;font-weight:700;margin-top:12px;display:flex;align-items:center;gap:12px}
.cart{width:24px;height:24px;background:var(--orange)}
.pop-grid{top:24px;left:365px;display:grid;grid-template-columns:repeat(4,74px);gap:14px 14px}
.pop-grid div{height:100px;background:#d6d6d6;padding:10px 12px}
.pop-grid div i{display:block;height:80px}

/* video */
.video{top:2173px;height:334px;background:linear-gradient(90deg,#2f2a25,#6b5a48 45%,#3c332b)}
.play{top:157px;left:566px;width:68px;height:68px;border-radius:50%;background:var(--white);display:flex;align-items:center;justify-content:center}
.video h3{top:244px;font-size:20px;font-weight:400;color:var(--white)}
.video .who{top:274px;font-size:10px;font-weight:700;color:var(--white)}
.video .who small{display:block;font-weight:400;color:#ccc;font-size:8px}

/* counters */
.counters{top:2507px;height:284px;background:var(--orange)}
.counter{top:47px;width:160px;text-align:center}
.ring{width:96px;height:96px;border-radius:50%;border:3px solid rgba(255,255,255,.85);background:rgba(255,255,255,.18);margin:0 auto;display:flex;align-items:center;justify-content:center;color:var(--white);font-family:"Raleway",sans-serif;font-size:18px;font-weight:700}
.counter p{margin-top:22px;color:var(--white);font-family:"Raleway",sans-serif;font-weight:700;font-size:14px}

/* blog */
.blog{top:2791px;height:418px;background:var(--white)}
.post{top:111px;width:227px}
.post-photo{height:157px}
.post h4{font-size:10px;font-weight:600;line-height:14px;margin-top:12px;padding-right:10px;text-transform:uppercase;color:#444}
.post.hl h4{color:var(--orange)}
.post .meta{font-size:8px;color:#999;margin-top:6px}
.post-mark{left:110px;top:250px;width:18px;height:2px;background:var(--orange)}

/* testimonials */
.testimonials{top:3209px;height:418px;background:linear-gradient(90deg,#2a2420,#4a3c30 50%,#2a2420)}
.quote-card{top:117px;width:344px;height:168px;background:var(--white);padding:22px 22px 0 56px;font-size:9px;color:var(--grey);line-height:14px}
.quote-mark{position:absolute;left:18px;top:12px;font-family:"Raleway",sans-serif;font-size:40px;color:var(--orange);font-weight:800;line-height:40px}
.avatar{top:264px;width:74px;height:74px;border-radius:50%;border:3px solid var(--orange);background:linear-gradient(135deg,#8a7866,#4d4238)}
.t-name{top:348px;width:200px;text-align:center;font-size:9px;font-weight:700;color:var(--orange);text-transform:uppercase}
.t-name small{display:block;color:#ccc;font-weight:400;font-size:8px;text-transform:none}
.dots{top:365px;left:582px;display:flex;gap:6px}
.dots i{width:6px;height:6px;border-radius:50%;background:#888}
.dots i.on{background:var(--white)}

/* authors */
.authors{top:3627px;height:478px;background:var(--white)}
.author{top:124px;width:177px}
.author-photo{height:194px;background:linear-gradient(180deg,#c9ccd1,#8f949b)}
.author-name{height:56px;background:var(--darker);color:var(--white);text-align:center;padding-top:14px;font-size:11px;font-weight:700}
.author-name small{display:block;font-weight:400;color:#aaa;font-size:8px}
.author.raised .author-name{height:100px;padding-top:54px}
.author-social{position:absolute;left:0;top:40px;width:30px}
.author-social i{display:block;width:30px;height:30px;background:var(--darker);border-bottom:1px solid #444}

/* member */
.member{top:4105px;height:291px;background:var(--orange)}
.member h2{top:42px;font-size:22px;font-weight:700;color:var(--white)}
.field{height:27px;width:227px;background:var(--white);font-size:9px;color:#777;line-height:27px;padding-left:10px}
.register{top:247px;left:534px;width:132px;height:28px;line-height:28px;background:var(--dark);color:var(--white);font-size:10px;text-align:center;font-weight:600}

/* newsletter */
.newsletter{top:4396px;height:234px;background:var(--white)}
.nl-input{top:153px;left:334px;width:384px;height:28px;border:1px solid var(--line);font-size:9px;color:#999;line-height:26px;padding-left:12px}
.nl-btn{top:153px;left:735px;width:127px;height:28px;line-height:28px}

/* location */
.location{top:4630px;height:320px;background:#e9e6df}
.loc-photo{left:0;top:0;width:470px;height:320px;background:linear-gradient(135deg,#6d5a48,#b39a7e)}
.loc-map{left:470px;top:0;width:730px;height:320px;background:linear-gradient(135deg,#e4e1d6,#cfd6c8)}
.loc-badge{top:-40px;left:476px;width:248px;height:248px;border-radius:50%;background:var(--white);box-shadow:0 4px 16px rgba(0,0,0,.2);text-align:center;padding-top:82px}
.loc-badge h4{font-size:13px;font-weight:700;line-height:17px}
.loc-badge p{font-size:10px;color:var(--grey);margin-top:4px}
.loc-badge .tel{color:var(--orange);font-weight:700;margin-top:14px;font-size:11px}

/* footer */
.footer{top:4950px;height:64px;background:var(--dark)}
.copyright{top:25px;left:300px;font-size:10px;color:#bbb}
.social{top:18px;left:668px;display:flex;gap:44px}
.social i{width:28px;height:28px;border-radius:50%;background:#444}
</style>
</head>
<body>

<header class="section hero">
  <div class="hero-photo" role="img" aria-label="Dim bookshop photo with stacked magazines and book covers"></div>
  <div class="abs topbar-note">Welcome to The Amber Ridge Publishing</div>
  <div class="abs topbar-mail">hello@amberridgepress.example</div>
  <div class="abs logo">Amber Ridge<br>Publishing</div>
  <nav class="abs nav">
    <span class="active">HOME</span><span>BOOKS</span><span>PORTFOLIO</span><span>AUTHOR</span><span>MAGAZINE</span><span>PAGES</span><span>BLOG</span><span>CONTACT US</span>
  </nav>
  <div class="abs nav-search">
    <svg width="30" height="30" viewBox="0 0 30 30"><circle cx="14" cy="14" r="5" fill="none" stroke="#fff" stroke-width="2"/><line x1="18" y1="18" x2="21" y2="21" stroke="#fff" stroke-width="2"/></svg>
  </div>
  <svg class="abs hero-arrow" style="left:106px" viewBox="0 0 22 36"><polyline points="16,4 4,18 16,32" fill="none" stroke="#fff" stroke-width="3"/></svg>
  <svg class="abs hero-arrow" style="left:1070px" viewBox="0 0 22 36"><polyline points="6,4 18,18 6,32" fill="none" stroke="#fff" stroke-width="3"/></svg>
  <p class="abs hero-kicker">Are You Searching a book publisher..?</p>
  <h1 class="abs hero-title">CUSTOM BOOK PRINTING</h1>
  <p class="abs hero-text">From first draft to finished shelf copy, we print, bind and ship your book with care and speed.</p>
  <a class="abs btn hero-btn" style="left:244px">See More</a>
  <a class="abs btn hero-btn" style="left:344px">Buy Now</a>
  <div class="abs tabs"><span class="tab">Book</span><span class="tab active">Author</span><span class="tab">Publications</span></div>
  <div class="abs search-band"></div>
  <div class="abs search-field" style="left:244px">First Name</div>
  <div class="abs search-field" style="left:434px">Phone Number</div>
  <div class="abs search-field" style="left:624px">Last Name</div>
  <a class="abs btn search-btn">Search Now</a>
</header>

<section class="section welcome">
  <div class="abs center" style="top:48px">
    <h2 class="sec-title">Welcome to the Amber Ridge Publishing</h2>
    <p class="sec-sub" style="margin-top:6px">Providing readers worldwide with stories worth their time</p>
    <div class="divider"></div>
  </div>
  <div class="abs feature" style="left:244px;top:129px">
    <div class="feature-icon"><svg width="28" height="28" viewBox="0 0 28 28"><rect x="6" y="4" width="16" height="20" fill="none" stroke="#555" stroke-width="2"/><line x1="10" y1="10" x2="18" y2="10" stroke="#555" stroke-width="2"/></svg></div>
    <h3>Printed Books</h3><p>Offset and digital runs with sharp covers and durable binding for any size.</p>
    <p class="more">See More<small>details</small></p>
  </div>
  <div class="abs feature hl" style="left:427px;top:129px">
    <div class="feature-icon"><svg width="28" height="28" viewBox="0 0 28 28"><path d="M5 16a9 9 0 0 1 18 0" fill="none" stroke="#f7941d" stroke-width="2"/><rect x="4" y="15" width="5" height="8" fill="#f7941d"/><rect x="19" y="15" width="5" height="8" fill="#f7941d"/></svg></div>
    <h3>E-Audiobooks</h3><p>Narrated editions produced in our studio and sent to every major store.</p>
    <p class="more" style="color:var(--orange)">See More<small>details</small></p>
  </div>
  <div class="abs feature" style="left:610px;top:129px">
    <div class="feature-icon"><svg width="28" height="28" viewBox="0 0 28 28"><rect x="5" y="5" width="18" height="18" fill="none" stroke="#555" stroke-width="2"/><line x1="9" y1="11" x2="19" y2="11" stroke="#555" stroke-width="2"/><line x1="9" y1="16" x2="19" y2="16" stroke="#555" stroke-width="2"/></svg></div>
    <h3>Magazine</h3><p>Full colour periodicals printed on time, every issue, for any print run.</p>
    <p class="more">See More<small>details</small></p>
  </div>
  <div class="abs feature" style="left:793px;top:129px">
    <div class="feature-icon"><svg width="28" height="28" viewBox="0 0 28 28"><rect x="4" y="8" width="10" height="14" fill="none" stroke="#555" stroke-width="2"/><rect x="14" y="4" width="10" height="14" fill="none" stroke="#555" stroke-width="2"/></svg></div>
    <h3>Printed Books, eBooks, &amp; POD</h3><p>One upload covers print, digital and print on demand for every reader.</p>
    <p class="more">See More<small>details</small></p>
  </div>
</section>

<section class="section categories on-dark">
  <div class="abs center" style="top:50px">
    <h2 class="sec-title">Our Top Categories</h2>
    <p class="sec-sub" style="margin-top:6px">Browse the genres our readers love most</p>
    <div class="divider"></div>
  </div>
  <div class="abs cat-filter">
    <span>&lsaquo;</span><span>All Categories</span><span class="active">Adventure</span><span>Biography &amp; Memoirs</span><span>Business</span><span>Computers &amp; Internet</span><span>&rsaquo;</span>
  </div>
  <div class="abs slide-arrow" style="left:188px"><svg width="24" height="24"><polyline points="14,7 9,12 14,17" fill="none" stroke="#fff" stroke-width="2"/></svg></div>
  <div class="abs slide-arrow" style="left:988px"><svg width="24" height="24"><polyline points="10,7 15,12 10,17" fill="none" stroke="#fff" stroke-width="2"/></svg></div>
  <div class="abs book-card" style="left:244px">
    <div class="book-cover" role="img" aria-label="Book cover for Silent Harbor, dark blue with lightning"></div>
    <h4>Silent Harbor</h4><p class="by">By T.R. Menshaw</p><p class="price">$18.95</p>
  </div>
  <div class="abs book-card" style="left:428px">
    <div class="book-cover" style="background:linear-gradient(135deg,#3d4a55,#1f262c)" role="img" aria-label="Book cover for Tidewater, deep teal"></div>
    <h4>Tidewater</h4><p class="by">By Owen Hale</p><p class="price">$35.00</p>
  </div>
  <div class="abs book-card raised" style="left:602px">
    <div class="book-cover" style="height:132px;background:linear-gradient(135deg,#c9a86a,#6f5a3a)" role="img" aria-label="Bookshelf of stacked hardcovers"></div>
    <h4>Paper Lantern</h4><p class="by">By Lena Crow</p>
    <p class="blurb">A quiet tale of letters, lamps and a town that reads by night.</p>
  </div>
  <div class="abs book-card" style="left:785px">
    <div class="book-cover" style="background:linear-gradient(135deg,#4b6b8f,#b04a3a)" role="img" aria-label="Book cover for Quiet Roads, blue with red"></div>
    <h4>Quiet Roads</h4><p class="by">By Mae Ortis</p><p class="price">$7.99</p>
  </div>
</section>

<section class="section feature-band" role="img" aria-label="Dimmed photo of bookshelves">
  <div class="abs center" style="top:40px">
    <h2>Checkout Huge Feature lists</h2>
    <p class="sec-sub" style="margin-top:8px;color:#ddd">Every tool an author needs, from layout and print to sales</p>
  </div>
  <div class="abs outline-btn">Learn More</div>
</section>

<section class="section popular">
  <div class="abs center" style="top:48px">
    <h2 class="sec-title">Most Popular Books</h2>
    <p class="sec-sub" style="margin-top:6px">The titles readers keep coming back for this season</p>
    <div class="divider"></div>
  </div>
  <div class="abs pop-tabs"><span class="active">Best Sellers</span><span>New Arrival</span><span>Coming Soon</span></div>
  <div class="abs pop-panel">
    <div class="abs pop-featured-cover" role="img" aria-label="Book cover for Every Hour is Dawn, cream with dark lettering"></div>
    <div class="abs pop-info">
      <h3>Every Hour is Dawn</h3>
      <p class="by">Clara Holt</p>
      <p class="stars">&#9733;&#9733;&#9733;&#9733;&#9733;</p>
      <p>A warm, clever guide to starting fresh each morning, written with humour and heart for busy readers everywhere.</p>
      <p class="price">$29.95 <span class="cart"></span></p>
    </div>
    <div class="abs pop-grid">
      <div><i role="img" aria-label="Book cover, pale yellow" style="background:#efe3b5"></i></div>
      <div><i role="img" aria-label="Book cover, dark with red" style="background:linear-gradient(#3a2a2a,#a33)"></i></div>
      <div><i role="img" aria-label="Book cover, deep blue" style="background:#2e3d6b"></i></div>
      <div><i role="img" aria-label="Book cover, white and green" style="background:#dfe8da"></i></div>
      <div><i role="img" aria-label="Book cover, light illustrated" style="background:#e8e0d2"></i></div>
      <div><i role="img" aria-label="Book cover, orange and white" style="background:#f1c490"></i></div>
      <div><i role="img" aria-label="Book cover, multicolour" style="background:linear-gradient(#c9d6e8,#e8a07a)"></i></div>
      <div><i role="img" aria-label="Book cover, dark planet" style="background:#2a2622"></i></div>
    </div>
  </div>
</section>

<section class="section video" role="img" aria-label="Photo of a reader in glasses in a library">
  <div class="abs play"><svg width="24" height="24"><polygon points="8,4 20,12 8,20" fill="#222"/></svg></div>
  <h3 class="abs center">Awesome Design And Great Support! Highly Recommend...</h3>
  <p class="abs center who">Amber Ridge Publishing<small>Reader review</small></p>
</section>

<section class="section counters">
  <div class="abs counter" style="left:244px"><div class="ring">14</div><p>Working Year</p></div>
  <div class="abs counter" style="left:425px"><div class="ring">1550</div><p>Books Sold</p></div>
  <div class="abs counter" style="left:605px"><div class="ring">210</div><p>Top Author</p></div>
  <div class="abs counter" style="left:789px"><div class="ring">250</div><p>Book Published</p></div>
</section>

<section class="section blog">
  <div class="abs center" style="top:24px">
    <h2 class="sec-title">Latest Blog Post</h2>
    <p class="sec-sub" style="margin-top:6px">News, tips and stories from our editors</p>
    <div class="divider"></div>
  </div>
  <article class="abs post" style="left:0"><div class="post-photo" role="img" aria-label="Photo of books on a table" style="background:linear-gradient(135deg,#8c7a66,#c7b9a4)"></div><h4>Five habits of authors who finish their first draft</h4><p class="meta">by Admin · 12 Aug 2016</p></article>
  <article class="abs post" style="left:244px"><div class="post-photo" role="img" aria-label="Photo of a reading nook" style="background:linear-gradient(135deg,#6f6a62,#b9aa92)"></div><h4>How we pick the covers that sell on shelves</h4><p class="meta">by Admin · 09 Aug 2016</p></article>
  <article class="abs post hl" style="left:487px"><div class="post-photo" role="img" aria-label="Photo of open notebook and pen" style="background:linear-gradient(135deg,#a79b8a,#e1d8c9)"></div><h4>Print on demand: the smart choice for new writers</h4><p class="meta">by Admin · 05 Aug 2016</p><div class="abs post-mark"></div></article>
  <article class="abs post" style="left:731px"><div class="post-photo" role="img" aria-label="Photo of a reader with a book" style="background:linear-gradient(135deg,#55504a,#a89a86)"></div><h4>Building a loyal audience before launch day</h4><p class="meta">by Admin · 01 Aug 2016</p></article>
  <article class="abs post" style="left:973px"><div class="post-photo" role="img" aria-label="Photo of a colourful book cover" style="background:linear-gradient(135deg,#d8c24a,#6aa0b8)"></div><h4>Editing tips from our senior team of readers</h4><p class="meta">by Admin · 28 Jul 2016</p></article>
</section>

<section class="section testimonials on-dark" role="img" aria-label="Dimmed photo of library shelves">
  <div class="abs center" style="top:44px">
    <h2 class="sec-title">Latest Blog Post</h2>
    <p class="sec-sub" style="margin-top:6px">What our authors and readers say about us</p>
    <div class="divider"></div>
  </div>
  <div class="abs quote-card" style="left:244px"><span class="quote-mark">&ldquo;</span>The team guided my book from rough manuscript to a beautiful print edition. Every step was clear, friendly and fast, and the result went beyond what I hoped for.</div>
  <div class="abs quote-card" style="left:612px"><span class="quote-mark">&ldquo;</span>Great service and honest advice. My novel reached readers in many countries within weeks, and the support team answered every question I had along the way.</div>
  <div class="abs avatar" style="left:379px"></div>
  <div class="abs avatar" style="left:747px"></div>
  <p class="abs t-name" style="left:316px">Elena Marwick<small>Author</small></p>
  <p class="abs t-name" style="left:684px">Ivy Rosen<small>Reader</small></p>
  <div class="abs dots"><i></i><i class="on"></i><i></i></div>
</section>

<section class="section authors">
  <div class="abs center" style="top:46px">
    <h2 class="sec-title">Our Top Author</h2>
    <p class="sec-sub" style="margin-top:6px">Meet the writers behind our best loved titles</p>
    <div class="divider"></div>
  </div>
  <div class="abs author" style="left:244px"><div class="author-photo" role="img" aria-label="Portrait photo of author"></div><div class="author-name">Nadia Korvel<small>Author</small></div></div>
  <div class="abs author" style="left:427px"><div class="author-photo" role="img" aria-label="Portrait photo of author"></div><div class="author-name">Petra Lunde<small>Author</small></div></div>
  <div class="abs author raised" style="left:610px"><div class="author-photo" role="img" aria-label="Portrait photo of author"></div><div class="author-name">Sion Marek<small>Author</small></div>
    <div class="author-social"><i></i><i></i><i></i><i></i></div></div>
  <div class="abs author" style="left:793px"><div class="author-photo" role="img" aria-label="Portrait photo of author"></div><div class="author-name">Joel Tarrant<small>Author</small></div></div>
</section>

<section class="section member">
  <h2 class="abs center">Become A Member</h2>
  <p class="abs center sec-sub" style="top:74px;color:#fff">Join today and get early access to new releases</p>
  <div class="abs field" style="top:147px;left:244px">Your Name</div>
  <div class="abs field" style="top:147px;left:491px">Your Email</div>
  <div class="abs field" style="top:147px;left:735px">Your Address</div>
  <div class="abs field" style="top:191px;left:244px">Your Phone</div>
  <div class="abs field" style="top:191px;left:491px">Your City</div>
  <div class="abs field" style="top:191px;left:735px">Select Package</div>
  <div class="abs register">Register</div>
</section>

<section class="section newsletter">
  <div class="abs center" style="top:52px">
    <h2 class="sec-title">Subscribe Our Newsletter</h2>
    <p class="sec-sub" style="margin-top:6px">Monthly picks and author news, straight to your inbox</p>
    <div class="divider"></div>
  </div>
  <div class="abs nl-input">Enter your email address here</div>
  <a class="abs btn nl-btn">Subscribe</a>
</section>

<section class="section location">
  <div class="abs loc-photo" role="img" aria-label="Photo of a person reading on a tablet"></div>
  <div class="abs loc-map" role="img" aria-label="Street map of the office area"></div>
  <div class="abs loc-badge">
    <svg width="18" height="24" viewBox="0 0 18 24"><path d="M9 1a8 8 0 0 0-8 8c0 6 8 14 8 14s8-8 8-14a8 8 0 0 0-8-8z" fill="#f7941d"/><circle cx="9" cy="9" r="3" fill="#fff"/></svg>
    <h4>Amber Ridge<br>Publishing</h4>
    <p>12 Maple Lane</p>
    <p class="tel">+1 555 014 2290</p>
  </div>
</section>

<footer class="section footer">
  <p class="abs copyright">&copy; 2016 www.amberridgepress.example All Right Reserved</p>
  <div class="abs social"><i></i><i></i><i></i><i></i></div>
</footer>

</body>
</html>
```